lakeview slab pumping "keep it flowing"

I want very easy to understand cards that say everything we offer.
i want the company name/logo, phone number and email on the front of card.
i want the card to stand out, it can be red with black lettering.
on the back of the card i want it to list everything that we can do like a list
the motto is JUST PUMP IT.
the can be in the lower right corner of the back of the card

Target Market(s)

concrete contractors

Industry/Entity Type

Concrete

Contact Information for Business Card

back of the card
Owner:Marco Feltz
Phone:503)418-6093
Email: LVSlabFlow@mailbox-example.com
address: 20918 ne marlow st Portland, OR 97236

Colors
ec1f27
000000
959595
5c5c5c
f04a50
ffffff
f37122

Requirements
Must have
• :we have years of experience in the world of concrete
• :our pumps can do up to 70 yards an hour
• :if you refer us to other contractors, will give you up to 10% off next pump job
• :don’t hesitate to call if you have any concrete related questions and to get a qoute
• Please put this on the front of the card, “just pump it” in the lower right corner

```html
<!DOCTYPE html>
<html lang="en">
<head>
<meta charset="utf-8">
<title>Lakeview Slab Pumping – Business Cards</title>
<link href="https://fonts.googleapis.com/css2?family=Montserrat:wght@400;500;600;700&display=swap" rel="stylesheet">
<style>
  :root {
    --red: #ec1f27;
    --card: #1f1f20;
    --ink: #ffffff;
    --muted: #cfcfcf;
    --stage: #d9d9d9;
  }
  * { box-sizing: border-box; margin: 0; padding: 0; }
  html, body { width: 1200px; height: 895px; overflow: hidden; }
  body {
    background: var(--stage);
    font-family: "Montserrat", sans-serif;
    position: relative;
  }
  .card {
    position: absolute;
    left: 240px;
    width: 720px;
    height: 411px;
    background: var(--card);
    overflow: hidden;
    box-shadow: 0 8px 22px rgba(0,0,0,.35);
  }
  .card--back { top: 24px; }
  .card--front { top: 460px; }

  .brand { position: absolute; display: flex; align-items: center; gap: 14px; }
  .brand__dot { width: 54px; height: 54px; border-radius: 50%; background: var(--red); flex: none; }
  .brand__name {
    color: var(--red); font-weight: 700; font-size: 52px; line-height: 1; letter-spacing: 1px;
  }
  .brand__sub {
    color: var(--ink); font-weight: 500; font-size: 15px; letter-spacing: 4px; margin-top: 4px;
  }

  /* back */
  .card--back .brand { left: 170px; top: 62px; }
  .about { position: absolute; left: 40px; top: 176px; width: 560px; }
  .about__title { color: var(--red); font-weight: 700; font-size: 17px; margin-bottom: 8px; }
  .about__list { list-style: none; color: var(--ink); font-size: 14px; line-height: 1.55; }
  .about__list li { position: relative; padding-left: 18px; }
  .about__list li::before {
    content: ""; position: absolute; left: 0; top: 8px; width: 6px; height: 6px;
    border-radius: 50%; background: var(--red);
  }
  .motto-band {
    position: absolute; right: 0; top: 312px; width: 420px; height: 30px;
    background: var(--red); color: var(--ink); font-weight: 700; font-size: 14px;
    letter-spacing: 1px; display: flex; align-items: center; justify-content: center;
  }
  .base-band { position: absolute; left: 0; bottom: 22px; width: 360px; height: 18px; background: var(--red); }

  /* front */
  .refer-corner { position: absolute; left: 0; top: 0; width: 150px; height: 100%; }
  .refer-text {
    position: absolute; left: 42px; top: 150px; color: var(--ink); font-weight: 600; font-size: 17px;
    transform: rotate(-90deg); transform-origin: left top; white-space: nowrap;
    top: 210px;
  }
  .card--front .brand { left: 220px; top: 44px; }
  .contact { position: absolute; left: 300px; top: 150px; width: 340px; text-align: center; color: var(--ink); }
  .contact__name { color: var(--red); font-weight: 700; font-size: 27px; letter-spacing: 1px; }
  .contact__role { font-size: 15px; margin-top: 2px; }
  .contact__rule { width: 120px; height: 2px; background: var(--red); margin: 8px auto 14px; }
  .contact__icons { display: flex; justify-content: center; gap: 10px; margin-bottom: 10px; }
  .contact__icons svg { width: 22px; height: 22px; }
  .contact__line { font-size: 16px; line-height: 1.5; }
  .address-band {
    position: absolute; right: 0; top: 318px; width: 520px; height: 32px; background: var(--red);
    color: var(--ink); font-size: 15px; font-weight: 500; display: flex; align-items: center; justify-content: center;
  }
  .card--front .base-band { width: 100%; bottom: 22px; height: 12px; }
</style>
</head>
<body>

<section class="card card--back">
  <div class="brand">
    <span class="brand__dot"></span>
    <div>
      <div class="brand__name">LAKEVIEW</div>
      <div class="brand__sub">SLAB PUMPING</div>
    </div>
  </div>

  <div class="about">
    <h2 class="about__title">ABOUT US:</h2>
    <ul class="about__list">
      <li>We have years of experience in the world of concrete</li>
      <li>Our pumps can do up to 70 yards an hour</li>
      <li>Call us for volume/repeat customer pricing</li>
      <li>Don't hesitate to call if you have any concrete related questions and to get a qoute</li>
    </ul>
  </div>

  <div class="motto-band">KEEP IT FLOWING</div>
  <div class="base-band"></div>
</section>

<section class="card card--front">
  <svg class="refer-corner" viewBox="0 0 150 411" preserveAspectRatio="none" aria-hidden="true">
    <polygon points="0,80 150,0 0,411" fill="#ec1f27"/>
  </svg>
  <div class="refer-text">Please refer us</div>

  <div class="brand">
    <span class="brand__dot"></span>
    <div>
      <div class="brand__name">LAKEVIEW</div>
      <div class="brand__sub">SLAB PUMPING</div>
    </div>
  </div>

  <div class="contact">
    <div class="contact__name">MARCO FELTZ</div>
    <div class="contact__role">Owner</div>
    <div class="contact__rule"></div>
    <div class="contact__icons">
      <svg viewBox="0 0 22 22" aria-label="phone" role="img">
        <circle cx="11" cy="11" r="11" fill="#ec1f27"/>
        <path d="M7.5 6.5l2 0 1 2.5-1.3 1a6 6 0 0 0 2.8 2.8l1-1.3 2.5 1 0 2c-4.5.4-8.4-3.5-8-8z" fill="#1f1f20"/>
      </svg>
      <svg viewBox="0 0 22 22" aria-label="email" role="img">
        <circle cx="11" cy="11" r="11" fill="#ec1f27"/>
        <rect x="6" y="7.5" width="10" height="7" fill="#1f1f20"/>
        <path d="M6 7.5l5 4 5-4" stroke="#ec1f27" stroke-width="1.2" fill="none"/>
      </svg>
    </div>
    <div class="contact__line">(503)418-6093</div>
    <div class="contact__line">LVSlabFlow@mailbox-example.com</div>
  </div>

  <div class="address-band">20918 ne marlow st Portland, OR 97236</div>
  <div class="base-band"></div>
</section>

</body>
</html>
```